TotNuzzle Business needs a Box Design

We need a box design for a new product Teething Mittens. Please check our file for a demo and Layout, Box mockup, Logo Vector
https://files.snorvaly.example/share/8kQpLm2ZtRw4Xv9HnC3jYbT6sDf1Ga7Ue

Target Market(s)

A parent have baby 6 - 12 month

Industry/Entity Type

Baby

Font styles to use
Decorative
Script

Requirements
Must have
• Our logo in a Box and follow our guide
Nice to have
• Cute design

```html
<!DOCTYPE html>
<html lang="en">
<head>
<meta charset="utf-8">
<title>TotNuzzle Baby Mitten Box</title>
<link rel="stylesheet" href="https://fonts.googleapis.com/css2?family=Comfortaa:wght@500;700&family=Mali:wght@500;600&display=swap">
<style>
  :root {
    --page: #ffffff;
    --stripe-blue: #c6e6f3;
    --stripe-yellow: #f5f1c8;
    --stripe-pink: #f7d5e4;
    --stripe-peach: #f8e2d8;
    --stripe-white: #fdfcfb;
    --gold: #c9a25a;
    --pink: #e264ae;
    --blue: #3fbde6;
    --body-blue: #2aa6d8;
    --ink: #222222;
    --window: #fbf8f4;
    --dash: #e8a79a;
  }
  * { margin: 0; padding: 0; box-sizing: border-box; }
  html, body { width: 1200px; height: 1200px; overflow: hidden; background: var(--page); }
  .canvas { position: relative; width: 1200px; height: 1200px; }

  .stripes {
    background: repeating-linear-gradient(90deg,
      var(--stripe-blue) 0 22px, var(--stripe-white) 22px 34px,
      var(--stripe-yellow) 34px 56px, var(--stripe-white) 56px 66px,
      var(--stripe-pink) 66px 88px, var(--stripe-white) 88px 98px,
      var(--stripe-peach) 98px 118px, var(--stripe-white) 118px 128px);
  }
  .hang-tab { position: absolute; box-shadow: 0 2px 6px rgba(0,0,0,.08); }
  .hang-hole {
    position: absolute; top: 22px; left: 50%; width: 44px; height: 14px;
    margin-left: -22px; background: var(--page); border-radius: 8px;
  }
  .panel { position: absolute; box-shadow: 0 6px 18px rgba(0,0,0,.12); overflow: hidden; }

  .brand-mark { display: flex; flex-direction: column; align-items: center; gap: 6px; }
  .brand-dot { width: 52px; height: 52px; border-radius: 50%; background: #f3dc86; }
  .brand-name { font-family: "Comfortaa", sans-serif; font-weight: 500; color: var(--gold); font-size: 30px; }

  /* back panel */
  .back-tab { left: 160px; top: 228px; width: 384px; height: 130px; opacity: .8; }
  .back-panel { left: 160px; top: 352px; width: 384px; height: 604px; }
  .back-panel .veil { position: absolute; inset: 0; background: linear-gradient(180deg, rgba(255,255,255,.8), rgba(238,240,248,.82)); }
  .back-panel .brand-mark { position: absolute; left: 0; right: 0; top: 32px; }
  .copy { position: absolute; left: 52px; width: 310px; font-family: "Mali", cursive; }
  .copy h2 { font-weight: 600; font-size: 15px; color: var(--pink); margin-bottom: 2px; }
  .copy p { font-weight: 500; font-size: 10.4px; line-height: 14.5px; color: var(--body-blue); }
  .copy-instructions { top: 168px; }
  .copy-wash { top: 262px; }
  .diagram { position: absolute; left: 26px; top: 354px; width: 220px; height: 160px; }
  .diagram-circle {
    position: absolute; left: 0; top: 0; width: 156px; height: 156px; border-radius: 50%;
    background: linear-gradient(160deg, #6fcdf0, #a59ee0 55%, #e69ac6);
  }
  .diagram svg { position: absolute; left: 0; top: 0; }
  .diagram-label { position: absolute; font-family: "Mali", cursive; font-size: 8px; font-weight: 600; color: var(--ink); }
  .badge { position: absolute; width: 48px; height: 48px; border-radius: 50%; background: #2b2418; border: 3px solid #c9a046; }
  .warning { position: absolute; left: 40px; right: 40px; top: 536px; text-align: center; font-family: "Mali", cursive; color: var(--ink); }
  .warning h3 { font-size: 14px; font-weight: 600; }
  .warning p { font-size: 10.4px; line-height: 14px; font-weight: 500; }

  /* front panel */
  .front-tab { left: 652px; top: 228px; width: 354px; height: 100px; }
  .front-tab .tab-brand { position: absolute; left: 52px; top: 30px; display: flex; flex-direction: column; align-items: center; gap: 2px; }
  .front-tab .brand-dot { width: 34px; height: 34px; }
  .front-tab .brand-name { font-size: 18px; }
  .tab-title { position: absolute; left: 188px; top: 40px; font-family: "Comfortaa", sans-serif; font-weight: 700; font-size: 26px; line-height: 28px; }
  .tab-title .line-baby { color: var(--pink); }
  .tab-title .line-mitten { color: var(--blue); }
  .front-panel { left: 652px; top: 320px; width: 392px; height: 632px; }
  .front-panel .brand-mark { position: absolute; left: 0; right: 0; top: 40px; }
  .front-panel .brand-name { font-size: 32px; }
  .window { position: absolute; left: 60px; top: 166px; }
  .product-title { position: absolute; left: 0; right: 0; top: 494px; text-align: center; font-family: "Comfortaa", sans-serif; font-weight: 700; }
  .product-title .line-baby { display: block; color: var(--blue); font-size: 50px; line-height: 54px; letter-spacing: 4px; }
  .product-title .line-mitten { display: block; color: var(--pink); font-size: 62px; line-height: 66px; letter-spacing: 4px; }
</style>
</head>
<body>
<main class="canvas">

  <section class="box-back" aria-label="Box back">
    <div class="hang-tab back-tab stripes"><span class="hang-hole"></span></div>
    <div class="panel back-panel stripes">
      <div class="veil"></div>
      <div class="brand-mark">
        <span class="brand-dot"></span>
        <span class="brand-name">TotNuzzle</span>
      </div>
      <div class="copy copy-instructions">
        <h2>Instructions for use:</h2>
        <p>Lorem ipsum dolor sit amet, consectetuer adipiscing elit, sed diam nonummy nibh euismod tincidunt ut laoreet dolore magna aliquam erat volutpat. Ut wisi enim ad minim veniam, quis nostrud exerci</p>
      </div>
      <div class="copy copy-wash">
        <h2>Wash instuctions:</h2>
        <p>Lorem ipsum dolor sit amet, consectetuer adipiscing elit, sed diam nonummy nibh euismod tincidunt ut laoreet dolore magna aliquam erat volutpat. Ut wisi enim ad minim veniam, quis nostrud exerci</p>
      </div>
      <div class="diagram">
        <div class="diagram-circle" role="img" aria-label="Mitten outline diagram showing its parts"></div>
        <svg width="220" height="160" viewBox="0 0 220 160" aria-hidden="true">
          <g fill="none" stroke="#1d2a36" stroke-width="1.3">
            <path d="M104 56 Q118 30 148 20"/>
            <path d="M108 98 Q118 92 132 90"/>
            <path d="M104 124 Q118 134 130 138"/>
          </g>
          <g fill="#1d2a36">
            <path d="M148 20 l-9 -1 l4 8 z"/>
            <path d="M132 90 l-8 -4 l0 8 z"/>
            <path d="M130 138 l-6 -6 l-2 8 z"/>
          </g>
        </svg>
        <span class="diagram-label" style="left:158px;top:12px">Lorem ipsum</span>
        <span class="diagram-label" style="left:138px;top:82px">Lorem ipsum</span>
        <span class="diagram-label" style="left:130px;top:142px">Lorem ipsum</span>
      </div>
      <span class="badge" style="left:290px;top:384px"></span>
      <span class="badge" style="left:294px;top:446px"></span>
      <div class="warning">
        <h3>Warning:</h3>
        <p>Lorem ipsum dolor sit amet, consectetuer adipiscing elit, sed diam nonummy nibh euismod tincidunt ut</p>
      </div>
    </div>
  </section>

  <section class="box-front" aria-label="Box front">
    <div class="hang-tab front-tab stripes">
      <span class="hang-hole"></span>
      <div class="tab-brand">
        <span class="brand-dot"></span>
        <span class="brand-name">TotNuzzle</span>
      </div>
      <div class="tab-title"><span class="line-baby">BABY</span><br><span class="line-mitten">MITTEN</span></div>
    </div>
    <div class="panel front-panel stripes">
      <div class="brand-mark">
        <span class="brand-dot"></span>
        <span class="brand-name">TotNuzzle</span>
      </div>
      <svg class="window" width="320" height="326" viewBox="0 0 320 326">
        <path d="M40 40 Q70 6 110 22 Q150 2 190 30 Q230 20 262 60 Q310 80 306 140 Q322 190 300 236 Q300 292 250 300 Q200 326 150 306 Q100 320 66 292 Q14 280 18 230 Q-4 180 20 130 Q8 74 40 40 Z"
              fill="var(--window)" stroke="var(--dash)" stroke-width="1.5" stroke-dasharray="6 4" role="img" aria-label="Window showing the mitten fabric with a playful cat print"/>
        <path d="M52 58 Q80 30 114 42 Q150 24 186 48 Q226 40 250 74 Q290 92 286 146 Q300 190 282 228 Q280 278 238 284 Q196 304 152 288 Q108 298 78 276 Q36 264 40 222 Q22 180 42 136 Q30 88 52 58 Z"
              fill="#efe4da" opacity=".6" aria-hidden="true"/>
      </svg>
      <h1 class="product-title"><span class="line-baby">BABY</span><span class="line-mitten">MITTEN</span></h1>
    </div>
  </section>

</main>
</body>
</html>
```